Harbor of Mercy - Team of Rabbis and Doctors Helping Families Dealing with Illness

The Harbor of Mercy is an organization that accompanies families dealing with severe illnesses of a family member. A team of rabbis and doctors provide support and real-time responses to these families.
The site theme is medicine and law, but the target market is religious Jewish families in crisis. Thus, the site design needs to combine:
- professional, conservative, serious
- spiritual
- warm hug

Target Market(s)

religious families suffering a health crisis

Industry/Entity Type

Non-profit organization

Number of Pages Required

1 page

Font styles to use
Sans Serif

Requirements
Must have
• Final design in PSD format. List of fonts used, colors used and link/button colors used in the design.

```html
<!DOCTYPE html>
<html lang="en">
<head>
<meta charset="utf-8">
<title>Harbor of Mercy</title>
<link href="https://fonts.googleapis.com/css2?family=Montserrat:wght@400;500;600;700;800&family=Open+Sans:wght@400;600&display=swap" rel="stylesheet">
<style>
:root{
  --navy:#0f2b46;
  --navy-deep:#0a1f33;
  --gold:#dca42a;
  --yellow:#f0b92b;
  --ink:#222;
  --muted:#555;
  --soft:#f3f3f3;
  --white:#fff;
}
*{margin:0;padding:0;box-sizing:border-box}
html,body{width:1200px;height:4860px;overflow:hidden}
body{font-family:"Open Sans",Arial,sans-serif;color:var(--ink);background:var(--white);position:relative}
h1,h2,h3,h4,.btn,.nav a{font-family:"Montserrat",Arial,sans-serif}
section,header,footer{position:absolute;left:0;width:1200px}
.btn{display:inline-block;border-radius:22px;padding:11px 26px;font-size:13px;font-weight:700;text-decoration:none}
.btn-navy{background:var(--navy);color:var(--white)}
.btn-yellow{background:var(--yellow);color:var(--navy-deep)}
.section-title{font-size:42px;font-weight:700;color:var(--gold)}
p.body{font-size:13px;line-height:1.75;color:var(--muted)}
.ph{position:absolute;border-radius:6px}

/* header */
.site-header{top:0;height:128px;background:var(--white)}
.topbar{position:absolute;top:14px;left:144px;display:flex;align-items:center;gap:14px;font-size:12px}
.search{display:flex;align-items:center;border:1px solid #ccc;border-radius:3px;width:130px;height:26px;justify-content:flex-end}
.search span{width:26px;height:26px;background:var(--yellow);display:flex;align-items:center;justify-content:center}
.dot{width:22px;height:22px;border-radius:50%;background:var(--yellow)}
.topbar .pill{background:var(--yellow);color:var(--navy-deep);border-radius:14px;padding:6px 16px;font-size:11px;font-weight:700;font-family:"Montserrat",sans-serif;text-transform:uppercase}
.nav{position:absolute;top:78px;left:144px;display:flex;gap:28px}
.nav a{font-size:14px;font-weight:600;color:var(--ink);text-decoration:none}
.logo{position:absolute;top:18px;right:60px;width:170px;height:92px;display:flex;align-items:center;gap:8px}
.logo .mark{width:14px;height:14px;background:var(--navy)}
.logo span{font-family:"Montserrat",sans-serif;font-weight:800;color:var(--navy);font-size:20px;line-height:1.1}

/* hero */
.hero{top:128px;height:544px;background:linear-gradient(100deg,#1a1410 0%,#3a2a1c 45%,#8a5a2a 75%,#3b2a1b 100%)}
.hero-copy{position:absolute;left:150px;top:160px;border-left:4px solid var(--yellow);padding-left:20px}
.hero-copy h1{color:var(--white);font-size:40px;line-height:1.2;font-weight:700;width:420px}
.phone-pill{position:absolute;left:150px;top:350px;display:flex;align-items:center;gap:10px;background:var(--navy);color:var(--white);border-radius:24px;padding:10px 22px;font-family:"Montserrat",sans-serif;font-weight:700;font-size:18px}

/* about */
.about{top:672px;height:640px}
.about .ph{left:144px;top:96px;width:428px;height:452px;background:linear-gradient(135deg,#6a4a2a,#c79a5b 60%,#3a2a1e)}
.play{position:absolute;left:334px;top:298px;width:48px;height:48px;border-radius:50%;background:rgba(255,255,255,.85);display:flex;align-items:center;justify-content:center}
.about-copy{position:absolute;left:608px;top:110px;width:452px}
.about-copy p{margin:18px 0}

/* moral */
.moral{top:1312px;height:608px;background:var(--soft)}
.moral-copy{position:absolute;left:144px;top:150px;width:440px}
.ticks{list-style:none;margin:14px 0 22px}
.ticks li{display:flex;gap:10px;font-size:12px;line-height:1.6;color:var(--muted);margin-bottom:8px}
.ticks svg{flex:none;margin-top:3px}
.moral .ph{left:632px;top:88px;width:428px;height:448px;background:linear-gradient(135deg,#2b2b2b,#6b5848 55%,#c49b6c)}
.dots{position:absolute;left:818px;top:508px;display:flex;gap:6px}
.dots i{width:8px;height:8px;border-radius:50%;background:#fff;opacity:.6}
.dots i:first-child{opacity:1}

/* services */
.services{top:1920px;height:520px}
.cards{position:absolute;left:144px;top:112px;display:flex;gap:14px}
.card{width:218px;height:328px;background:var(--white);box-shadow:0 2px 10px rgba(0,0,0,.12);text-align:center}
.card .img{height:148px}
.card h3{font-size:17px;margin:20px 0 10px}
.card p{font-size:12px;line-height:1.6;color:var(--muted);padding:0 16px}
.card a{display:inline-block;margin-top:14px;font-size:12px;font-weight:700;color:var(--ink);text-decoration:underline}

/* testimonials */
.testimonials{top:2440px;height:560px;background:var(--soft)}
.testimonials h2{text-align:center;margin-top:90px}
.quote{position:absolute;top:170px;width:400px;height:270px;background:var(--white);border-bottom:5px solid var(--yellow);box-shadow:0 2px 10px rgba(0,0,0,.1);text-align:center;padding:100px 30px 0}
.avatar{position:absolute;left:168px;top:20px;width:64px;height:64px;border-radius:50%;background:linear-gradient(135deg,#8a6a4a,#3a2a1e);border:3px solid var(--yellow)}
.quote h4{position:absolute;left:0;right:0;top:-4px;font-size:14px}
.quote p{font-size:13px;line-height:1.8;color:var(--muted)}
.arrow{position:absolute;top:282px;width:40px;height:40px;border-radius:50%;background:var(--white);box-shadow:0 1px 6px rgba(0,0,0,.2);display:flex;align-items:center;justify-content:center}

/* news */
.news{top:3000px;height:780px}
.news h2{text-align:center;margin-top:108px}
.news-item{position:absolute;background:var(--white);box-shadow:0 2px 10px rgba(0,0,0,.12)}
.news-item .meta{font-size:11px;color:var(--muted);display:flex;align-items:center;gap:6px}
.news-item h3{font-size:16px;line-height:1.35;margin:8px 0}
.news-item p{font-size:11px;line-height:1.6;color:var(--muted)}
.news-item a{display:inline-block;margin-top:8px;font-size:11px;font-weight:700;color:var(--gold);text-decoration:underline}

/* cta */
.cta{top:3780px;height:440px;background:linear-gradient(180deg,#0f2b46,#1e4466 60%,#0f2b46);text-align:center}
.cta h2{color:var(--white);font-size:28px;line-height:1.45;font-weight:700;width:820px;margin:150px auto 26px}

/* newsletter */
.newsletter{top:4220px;height:312px;text-align:center}
.newsletter h2{margin-top:66px;letter-spacing:1px}
.newsletter .sub{font-size:12px;color:var(--muted);margin:8px 0 18px}
.field{width:520px;height:40px;margin:0 auto;border:1px solid #ccc;border-radius:4px;text-align:left;padding:11px 16px;font-size:12px;color:#777}
.newsletter .btn{margin-top:20px;padding:10px 42px}
.hotline{position:absolute;right:40px;top:178px;display:flex;align-items:center;gap:8px;background:var(--yellow);border-radius:24px;padding:6px 16px 6px 6px;font-family:"Montserrat",sans-serif;font-weight:700;font-size:12px;color:var(--navy-deep)}
.hotline i{width:34px;height:34px;border-radius:50%;background:var(--white);display:flex;align-items:center;justify-content:center}

/* footer */
.site-footer{top:4532px;height:288px;background:var(--navy-deep);color:var(--white)}
.col{position:absolute;top:54px}
.col h4{font-size:17px;margin-bottom:14px}
.col ul{list-style:none;font-size:12px;line-height:1.9;color:#d6dbe2}
.contact li{display:flex;gap:8px;margin-bottom:6px;line-height:1.5}
.footer-logo{position:absolute;left:880px;top:60px;display:flex;align-items:center;gap:8px}
.footer-logo span{font-family:"Montserrat",sans-serif;font-weight:800;font-size:24px;line-height:1.1}
.footer-logo .mark{width:14px;height:14px;background:var(--yellow)}
.follow{position:absolute;left:880px;top:168px;display:flex;align-items:center;gap:8px;font-size:12px}
.follow i{width:24px;height:24px;border-radius:50%;background:var(--yellow)}
.copyright{position:absolute;top:4820px;left:0;width:1200px;height:40px;background:var(--yellow);text-align:center;font-size:12px;font-weight:600;line-height:40px;color:var(--navy-deep)}
</style>
</head>
<body>

<header class="site-header">
  <div class="topbar">
    <div class="search"><span><svg width="12" height="12" viewBox="0 0 12 12"><circle cx="5" cy="5" r="3.5" fill="none" stroke="#0a1f33" stroke-width="1.5"/><line x1="7.5" y1="7.5" x2="11" y2="11" stroke="#0a1f33" stroke-width="1.5"/></svg></span></div>
    <i class="dot"></i><i class="dot"></i>
    <span>info@harborofmercy.org</span>
    <span>Main Line: (123) 456-7890</span>
    <span class="pill">Donate Now</span>
    <span class="pill">Register Now</span>
  </div>
  <nav class="nav">
    <a href="#">Home</a><a href="#">About Us</a><a href="#">Courses</a><a href="#">Conferences</a><a href="#">Lectures</a><a href="#">News</a><a href="#">Contact Us</a>
  </nav>
  <div class="logo"><i class="mark"></i><span>Harbor of Mercy</span></div>
</header>

<section class="hero" role="img" aria-label="Hands lighting candles beside a handwritten note">
  <div class="hero-copy"><h1>Should cancer patients continue treatment?</h1></div>
  <div class="phone-pill">
    <svg width="18" height="18" viewBox="0 0 24 24"><path fill="#f0b92b" d="M6.6 10.8a15 15 0 006.6 6.6l2.2-2.2a1 1 0 011-.25 11.4 11.4 0 003.6.57 1 1 0 011 1V20a1 1 0 01-1 1A17 17 0 013 4a1 1 0 011-1h3.5a1 1 0 011 1c0 1.25.2 2.45.57 3.6a1 1 0 01-.25 1z"/></svg>
    123 456 7890
  </div>
</section>

<section class="about">
  <div class="ph" role="img" aria-label="Father and son reading together at a festive candlelit table"></div>
  <div class="play"><svg width="16" height="18" viewBox="0 0 16 18"><path d="M2 1l13 8-13 8z" fill="#0f2b46"/></svg></div>
  <div class="about-copy">
    <h2 class="section-title">About Us</h2>
    <p class="body">Lorem ipsum dolor sit amet, consectetur adipiscing elit, sed do eiusmod tempor incididunt ut labore et dolore magna aliqua. Ut enim ad minim veniam, quis nostrud exercitation ullamco laboris nisi ut aliquip ex ea commodo consequat. Lorem ipsum dolor sit amet, consectetur adipiscing elit, sed do eiusmod tempor incididunt ut labore et dolore magna aliqua.</p>
    <p class="body">Lorem ipsum dolor sit amet, consectetur adipiscing elit, sed do eiusmod tempor incididunt ut labore et dolore magna aliqua. Ut enim ad minim veniam, quis nostrud exercitation ullamco laboris nisi ut.</p>
    <p class="body">Lorem ipsum dolor sit amet, consectetur adipiscing elit, sed do eiusmod tempor incididunt ut labore et dolore magna aliqua.</p>
    <a class="btn btn-navy" href="#">Contact Us</a>
  </div>
</section>

<section class="moral">
  <div class="moral-copy">
    <h2 class="section-title">Moral Issues</h2>
    <p class="body" style="margin-top:12px">Lorem ipsum dolor sit amet, consectetur adipiscing elit, sed do eiusmod tempor incididunt ut labore et dolore magna aliqua.</p>
    <ul class="ticks">
      <li><svg width="12" height="12" viewBox="0 0 12 12"><circle cx="6" cy="6" r="5.5" fill="none" stroke="#555"/><path d="M3.5 6l2 2 3-4" fill="none" stroke="#555" stroke-width="1.2"/></svg>Consectetur adipiscing elit sed do eiusmod tempor incididunt ut labore et dolore magna aliqua</li>
      <li><svg width="12" height="12" viewBox="0 0 12 12"><circle cx="6" cy="6" r="5.5" fill="none" stroke="#555"/><path d="M3.5 6l2 2 3-4" fill="none" stroke="#555" stroke-width="1.2"/></svg>Lorem ipsum dolor sit amet consectetur adipiscing elit sed do eiusmod</li>
      <li><svg width="12" height="12" viewBox="0 0 12 12"><circle cx="6" cy="6" r="5.5" fill="none" stroke="#555"/><path d="M3.5 6l2 2 3-4" fill="none" stroke="#555" stroke-width="1.2"/></svg>Consectetur adipiscing elit sed do eiusmod tempor incididunt ut labore et dolore magna aliqua</li>
      <li><svg width="12" height="12" viewBox="0 0 12 12"><circle cx="6" cy="6" r="5.5" fill="none" stroke="#555"/><path d="M3.5 6l2 2 3-4" fill="none" stroke="#555" stroke-width="1.2"/></svg>Lorem ipsum dolor sit amet consectetur adipiscing elit sed do eiusmod</li>
    </ul>
    <a class="btn btn-navy" href="#">Ask The Rabbi</a>
  </div>
  <div class="ph" role="img" aria-label="Group of adults in conversation around a table"></div>
  <div class="dots"><i></i><i></i><i></i></div>
</section>

<section class="services">
  <div class="cards">
    <div class="card"><div class="img" role="img" aria-label="Students studying together" style="background:linear-gradient(135deg,#4a3a2e,#a88b6b)"></div><h3>Courses</h3><p>Lorem ipsum dolor sit amet, consectetur adipiscing elit sed do eiusmod tempor</p><a href="#">Know More</a></div>
    <div class="card"><div class="img" role="img" aria-label="Audience at a conference hall" style="background:linear-gradient(135deg,#7a3a22,#d29a64)"></div><h3>Conferences</h3><p>Lorem ipsum dolor sit amet, consectetur adipiscing elit sed do eiusmod tempor</p><a href="#">Know More</a></div>
    <div class="card"><div class="img" role="img" aria-label="Lecture room with seated listeners" style="background:linear-gradient(135deg,#3b4a5a,#b59a7a)"></div><h3>Lectures</h3><p>Lorem ipsum dolor sit amet, consectetur adipiscing elit sed do eiusmod tempor</p><a href="#">Know More</a></div>
    <div class="card"><div class="img" role="img" aria-label="Support line operator with headset" style="background:linear-gradient(135deg,#9fc3d8,#e7eef2)"></div><h3>Hotline 24/7</h3><p>Lorem ipsum dolor sit amet, consectetur adipiscing elit sed do eiusmod tempor</p><a href="#">Know More</a></div>
  </div>
</section>

<section class="testimonials">
  <h2 class="section-title">Testimonials</h2>
  <div class="arrow" style="left:52px"><svg width="10" height="14" viewBox="0 0 10 14"><path d="M8 1L2 7l6 6" fill="none" stroke="#222" stroke-width="2"/></svg></div>
  <div class="quote" style="left:184px">
    <div class="avatar" role="img" aria-label="Portrait of Elijah"></div>
    <h4 style="top:90px">Elijah</h4>
    <p style="margin-top:16px">Lorem ipsum dolor sit amet, consectetur adipiscing elit sed do eiusmod tempor incididunt ut labore et dolore magna aliqua. Ut enim ad minim veniam quis nostrud exercitation ullamco laboris nisi ut aliquip ex ea commodo.</p>
  </div>
  <div class="quote" style="left:616px">
    <div class="avatar" role="img" aria-label="Portrait of James"></div>
    <h4 style="top:90px">James</h4>
    <p style="margin-top:16px">Lorem ipsum dolor sit amet, consectetur adipiscing elit sed do eiusmod tempor incididunt ut labore et dolore magna aliqua. Ut enim ad minim veniam quis nostrud exercitation ullamco laboris nisi ut aliquip ex ea commodo.</p>
  </div>
  <div class="arrow" style="left:1108px"><svg width="10" height="14" viewBox="0 0 10 14"><path d="M2 1l6 6-6 6" fill="none" stroke="#222" stroke-width="2"/></svg></div>
</section>

<section class="news">
  <h2 class="section-title">Latest News</h2>
  <div class="news-item" style="left:144px;top:210px;width:500px;height:240px">
    <div role="img" aria-label="Celebration with blue and white flags" style="position:absolute;left:0;top:0;width:220px;height:240px;background:linear-gradient(135deg,#2f5e9a,#c9d7e8 60%,#6b4a2a)"></div>
    <div style="position:absolute;left:240px;top:20px;width:240px">
      <div class="meta"><svg width="11" height="11" viewBox="0 0 11 11"><rect x=".5" y="1.5" width="10" height="9" fill="none" stroke="#555"/><line x1=".5" y1="4" x2="10.5" y2="4" stroke="#555"/></svg>June 10, 2023</div>
      <h3>Lorem Ipsum Dolor Sit Amet Contetuer Sit</h3>
      <p>Lorem ipsum dolor sit amet, consectetur adipiscing elit, sed diam nonummy nibh euismod tincidunt ut laoreet dolore.</p>
      <a href="#">Know More</a>
    </div>
  </div>
  <div class="news-item" style="left:144px;top:470px;width:500px;height:230px">
    <div role="img" aria-label="Family gathered at a window" style="position:absolute;left:0;top:0;width:220px;height:230px;background:linear-gradient(135deg,#5a4a42,#d9d4cf)"></div>
    <div style="position:absolute;left:240px;top:20px;width:240px">
      <div class="meta"><svg width="11" height="11" viewBox="0 0 11 11"><rect x=".5" y="1.5" width="10" height="9" fill="none" stroke="#555"/><line x1=".5" y1="4" x2="10.5" y2="4" stroke="#555"/></svg>June 10, 2023</div>
      <h3>Lorem Ipsum Dolor Sit Am Contetuer Sit</h3>
      <p>Lorem ipsum dolor sit amet, consectetur adipiscing elit, sed diam nonummy nibh euismod tincidunt ut laoreet dolore.</p>
      <a href="#">Know More</a>
    </div>
  </div>
  <div class="news-item" style="left:664px;top:210px;width:396px;height:490px">
    <div role="img" aria-label="Volunteers packing donation boxes" style="height:220px;background:linear-gradient(135deg,#5c4634,#c8a57e 55%,#3d4f66)"></div>
    <div style="padding:20px 22px">
      <div class="meta"><svg width="11" height="11" viewBox="0 0 11 11"><rect x=".5" y="1.5" width="10" height="9" fill="none" stroke="#555"/><line x1=".5" y1="4" x2="10.5" y2="4" stroke="#555"/></svg>June 10, 2023</div>
      <h3>Lorem Ipsum Dolor Sit Am Contetuer Sit</h3>
      <p>Lorem ipsum dolor sit amet, consectetur adipiscing elit, sed diam nonummy nibh euismod tincidunt ut laoreet dolore magna aliquam erat volutpat. Ut wisi enim ad minim veniam, quis nostrud exerci tation.</p>
      <a href="#">Know More</a>
    </div>
  </div>
  <div role="img" aria-label="Hand holding a paper star" style="position:absolute;left:1062px;top:560px;width:120px;height:180px;background:linear-gradient(160deg,#f2f2f2,#d8c2a8)"></div>
</section>

<section class="cta" role="img" aria-label="City skyline at dusk under a blue tint">
  <h2>Lorem Ipsum Dolor Sit Amet Consectetur Adipiscing Elit Sed Do Eiusmod Tempor Incididunt Ut Labore Et Dolore Magna</h2>
  <a class="btn btn-yellow" href="#">Ask The Rabbi</a>
</section>

<section class="newsletter">
  <h2 class="section-title">NEWSLETTER SIGN UP</h2>
  <p class="sub">Subscribe to our newsletter to get the latest updates in your inbox</p>
  <div class="field">Enter Your Email Address</div>
  <a class="btn btn-navy" href="#">Subscribe</a>
  <div class="hotline"><i><svg width="16" height="16" viewBox="0 0 24 24"><path fill="#0a1f33" d="M6.6 10.8a15 15 0 006.6 6.6l2.2-2.2a1 1 0 011-.25 11.4 11.4 0 003.6.57 1 1 0 011 1V20a1 1 0 01-1 1A17 17 0 013 4a1 1 0 011-1h3.5a1 1 0 011 1c0 1.25.2 2.45.57 3.6a1 1 0 01-.25 1z"/></svg></i>Hotline 24/7</div>
</section>

<footer class="site-footer">
  <div class="col" style="left:144px">
    <h4>Quick Links</h4>
    <ul><li>Home</li><li>About Us</li><li>Courses</li><li>Conferences</li><li>Lectures</li><li>News</li><li>Contact Us</li></ul>
  </div>
  <div class="col contact" style="left:464px">
    <h4>Contact Us</h4>
    <ul>
      <li><svg width="12" height="14" viewBox="0 0 12 14"><path d="M6 0a5 5 0 00-5 5c0 4 5 9 5 9s5-5 5-9a5 5 0 00-5-5z" fill="#f0b92b"/><circle cx="6" cy="5" r="1.8" fill="#0a1f33"/></svg><span>14 Harbor Lane,<br>Springvale, AR 12345</span></li>
      <li><svg width="12" height="12" viewBox="0 0 24 24"><path fill="#f0b92b" d="M6.6 10.8a15 15 0 006.6 6.6l2.2-2.2a1 1 0 011-.25 11.4 11.4 0 003.6.57 1 1 0 011 1V20a1 1 0 01-1 1A17 17 0 013 4a1 1 0 011-1h3.5a1 1 0 011 1c0 1.25.2 2.45.57 3.6a1 1 0 01-.25 1z"/></svg><span>Phone<br>+1 123 456 7890</span></li>
      <li><svg width="13" height="10" viewBox="0 0 13 10"><rect x=".5" y=".5" width="12" height="9" fill="none" stroke="#f0b92b"/><path d="M.5 .5l6 5 6-5" fill="none" stroke="#f0b92b"/></svg><span>Email<br>info@harborofmercy.org</span></li>
    </ul>
  </div>
  <div class="footer-logo"><i class="mark"></i><span>Harbor of Mercy</span></div>
  <div class="follow"><i></i>Follow Us</div>
</footer>
<div class="copyright">© 2023 The Harbor of Mercy. All Rights Reserved</div>

</body>
</html>
```